Bitcoin Casino User Interface

This is a responsive design for a new bitcoin casino called the brass latch casino

The 4 games I need the Ui for are video poker, blackjack, roulette and dice

The designs should be ideal for mobile and have a bit of a retro feel

Good example is www.plumreelhallvexcom

Target Market(s)

Adults between the ages of 21-55 all over the world

Industry/Entity Type

Casino

Font styles to use
Serif

Colors
5dc4b5
ffffff

Requirements
Must have
• Must be responsive and look great on mobile
design must be functional
Should not have
• Any generic and standard elements

```html
<!DOCTYPE html>
<html lang="en">
<head>
<meta charset="utf-8">
<title>Brass Latch Casino – Video Poker</title>
<link href="https://fonts.googleapis.com/css2?family=Montserrat:wght@500;600;700&display=swap" rel="stylesheet">
<style>
  :root {
    --bg: #e7dfcc;
    --teal: #5dc4b5;
    --teal-deep: #1f9a7e;
    --panel: #f1efea;
    --ink: #77706c;
    --white: #ffffff;
    --orange: #eea821;
    --card-face: #e4ecef;
    --card-edge: #c9d3d7;
  }
  * { box-sizing: border-box; margin: 0; padding: 0; }
  html, body { width: 1200px; height: 549px; overflow: hidden; }
  body {
    background: var(--bg);
    font-family: "Montserrat", sans-serif;
    position: relative;
  }
  .brand {
    position: absolute; left: 108px; top: 32px;
    display: flex; align-items: flex-end; gap: 8px;
    color: var(--teal-deep); font-weight: 700; font-size: 26px; line-height: 30px;
    text-transform: uppercase; letter-spacing: 0.3px; white-space: nowrap;
  }
  .brand-name span { display: block; }
  .brand-name span + span { padding-left: 36px; }
  .brand-dot {
    width: 24px; height: 24px; border-radius: 50%; background: var(--orange); flex: none;
    margin-bottom: 4px;
  }
  .main-nav {
    position: absolute; left: 384px; top: 52px; width: 676px; height: 50px;
    background: var(--teal); border-radius: 25px;
    display: flex; align-items: center; padding-left: 47px;
  }
  .main-nav a {
    color: var(--white); text-decoration: none; font-size: 15.5px; font-weight: 500;
    margin-right: 26px; white-space: nowrap;
  }
  .die {
    position: absolute; left: 1020px; top: 46px; width: 62px; height: 56px;
    background: var(--white); border-radius: 12px;
    box-shadow: 0 2px 4px rgba(0,0,0,.18);
    transform: rotate(-12deg);
  }
  .paytable {
    position: absolute; left: 80px; top: 157px; width: 666px; height: 292px;
    background: var(--panel); border-radius: 12px;
  }
  .paytable .active-col {
    position: absolute; left: 226px; top: 3px; width: 78px; height: 287px;
    background: var(--teal);
  }
  .paytable table {
    position: absolute; left: 42px; top: 19px; border-collapse: collapse;
    color: var(--ink); font-size: 15px; font-weight: 600;
  }
  .paytable td { height: 28px; padding: 0; vertical-align: middle; white-space: nowrap; }
  .paytable td.hand { width: 213px; }
  .paytable td.c1 { width: 79px; color: var(--white); font-weight: 500; }
  .paytable td.c2, .paytable td.c3, .paytable td.c4 { width: 70px; font-weight: 500; }
  .paytable td.c5 { font-weight: 500; }
  .hand-row { position: absolute; left: 800px; top: 194px; display: flex; gap: 10px; }
  .card {
    width: 74px; height: 105px; background: var(--card-face);
    border: 1px solid var(--card-edge); border-radius: 3px;
    box-shadow: 0 1px 2px rgba(0,0,0,.12);
  }
  .card:nth-child(3) { margin-left: -2px; }
  .card:nth-child(4) { margin-left: -6px; }
  .controls { position: absolute; left: 802px; top: 321px; display: flex; align-items: center; }
  .btn {
    background: var(--orange); color: var(--white); border: 2px solid var(--white);
    border-radius: 20px; height: 40px; font-family: inherit; font-size: 14.5px; font-weight: 600;
    padding: 0; white-space: nowrap; text-align: center;
  }
  .btn-more { width: 127px; }
  .btn-auto { width: 77px; margin-left: 18px; }
  .bet { margin-left: 24px; color: var(--teal); font-size: 25px; font-weight: 700; letter-spacing: 1px; white-space: nowrap; }
</style>
</head>
<body>
  <div class="brand">
    <div class="brand-name"><span>Brass Latch</span><span>Casino</span></div>
    <span class="brand-dot"></span>
  </div>

  <nav class="main-nav">
    <a href="#">Video Poker</a>
    <a href="#">Blackjack</a>
    <a href="#">Roulette</a>
    <a href="#">Craps</a>
    <a href="#">Keno</a>
    <a href="#">Slots</a>
    <a href="#">Dice</a>
  </nav>
  <div class="die" role="img" aria-label="White game die"></div>

  <section class="paytable">
    <div class="active-col"></div>
    <table>
      <tr><td class="hand">ROYAL FLUSH</td><td class="c1">250</td><td class="c2">500</td><td class="c3">500</td><td class="c4">500</td><td class="c5">4173.30</td></tr>
      <tr><td class="hand">STRAIGHT FLUSH</td><td class="c1">50</td><td class="c2">100</td><td class="c3">100</td><td class="c4">100</td><td class="c5">250</td></tr>
      <tr><td class="hand">4 OF A KIND</td><td class="c1">25</td><td class="c2">50</td><td class="c3">50</td><td class="c4">50</td><td class="c5">125</td></tr>
      <tr><td class="hand">FULL HOUSE</td><td class="c1">9</td><td class="c2">18</td><td class="c3">18</td><td class="c4">18</td><td class="c5">45</td></tr>
      <tr><td class="hand">FLUSH</td><td class="c1">6</td><td class="c2">12</td><td class="c3">12</td><td class="c4">12</td><td class="c5">30</td></tr>
      <tr><td class="hand">STRAIGHT</td><td class="c1">4</td><td class="c2">8</td><td class="c3">8</td><td class="c4">8</td><td class="c5">20</td></tr>
      <tr><td class="hand">3 OF A KIND</td><td class="c1">3</td><td class="c2">6</td><td class="c3">6</td><td class="c4">6</td><td class="c5">15</td></tr>
      <tr><td class="hand">TWO PAIR</td><td class="c1">2</td><td class="c2">4</td><td class="c3">4</td><td class="c4">4</td><td class="c5">10</td></tr>
      <tr><td class="hand">JACKS OR BETTER</td><td class="c1">1</td><td class="c2">2</td><td class="c3">2</td><td class="c4">2</td><td class="c5">5</td></tr>
    </table>
  </section>

  <div class="hand-row">
    <div class="card" role="img" aria-label="Ace of spades playing card"></div>
    <div class="card" role="img" aria-label="Ace of hearts playing card"></div>
    <div class="card" role="img" aria-label="Ace of clubs playing card"></div>
    <div class="card" role="img" aria-label="Ace of diamonds playing card"></div>
  </div>

  <div class="controls">
    <button class="btn btn-more">more games</button>
    <button class="btn btn-auto">auto</button>
    <span class="bet">BET 5</span>
  </div>
</body>
</html>
```